Blow Dry Bar Business Cards

These cards must be eye catching and modern.
You must be willing to work fast and make changes.

Winner will be offered other projects

Files 1 THIS IS THE STYLE CARDS I AM INTRESTED IN!!!
Please be creative, I am paying for my own eye catching design. I need files to be prisma press ready.

COLORS THAT ARE PAINTED INSIDE MY SHOP:
- - - http://www.brenwickcoatings.example/en/explore-colors/painter/color-selector.html?colors=4007-3C

- - - http://www.tarnellhues.example/color/paint-colors/quiet-harbor-d58-2

I want the business cards sleek and modern if you use the logo please correct imperfections. I added the part that says Blow Dry Bar (see website).
Do not be afraid to separate the blow dryer from the name to make the cards look like the file with the pink elephant.

SHOULD INCLUDE
*Blow Dryer (we are a blow dry bar not a salon we do not cut or color so do not include sheers of any kind)
*BUSINESS NAME: Simply Silken Waves - Blow Dry Bar (PLEASE SEE MY WEBSITE)
* Website: SIMPLYSILKENWAVES.EXAMPLE
*Phone number (555) 014-2763
Updates

Prisma press said it can be submitted in JPG

http://www.tarnellhues.example/color/paint-colors/quiet-harbor-d58-2 http://www.brenwickcoatings.example/en/explore-colors/painter/color-selector.html?colors=4007-3C ^^^^ These links will take you to the color paint that is painted inside my shop.

Target Market(s)

AGES 18 - 55 WOMEN
HIGH END MARKET

Industry/Entity Type

Salon

Requirements
Must have
• SEE COLOR EXAMPLE FILE
BLOW DRYER
UNIQUE
I LIKE THE CARD WITH THE PINK ELEPHANT THE BEST
Nice to have
• BE AS CREATIVE AND MODERN AS POSSIBLE DO NOT COPY ANY OF THE CARDS BELOW.
Should not have
• SCISSORS
PINK

```html
<!DOCTYPE html>
<html lang="en">
<head>
<meta charset="utf-8">
<title>Simply Silken Waves – Business Cards</title>
<link rel="stylesheet" href="https://fonts.googleapis.com/css2?family=Lato:wght@400;700&display=swap">
<style>
  :root {
    --backdrop: #1f1f21;
    --card: #3b2226;
    --card-edge: #4a2d31;
    --teal: #4cc4cc;
    --ink-light: #ffffff;
  }
  * { box-sizing: border-box; margin: 0; padding: 0; }
  html, body {
    width: 1200px;
    height: 800px;
    overflow: hidden;
    background: var(--backdrop);
  }
  .canvas {
    width: 1200px;
    height: 800px;
    display: flex;
    align-items: center;
    justify-content: center;
    gap: 60px;
    font-family: "Lato", sans-serif;
  }
  .card {
    width: 510px;
    height: 292px;
    border-radius: 18px;
    background: var(--card);
    box-shadow: inset 0 0 0 1px var(--card-edge);
    display: flex;
    flex-direction: column;
    align-items: center;
    justify-content: center;
    color: var(--ink-light);
  }
  .wordmark {
    display: flex;
    align-items: center;
    gap: 10px;
    color: var(--teal);
    font-weight: 400;
    letter-spacing: 0.5px;
  }
  .wordmark__dot {
    width: 10px;
    height: 10px;
    border-radius: 50%;
    background: var(--teal);
  }
  .card--front .wordmark { font-size: 30px; margin-bottom: 18px; }
  .card--back .wordmark { font-size: 40px; }
  .business-name {
    font-size: 19px;
    font-weight: 700;
    letter-spacing: 0.3px;
    margin-bottom: 22px;
  }
  .contact {
    list-style: none;
    display: flex;
    flex-direction: column;
    align-items: center;
    gap: 8px;
  }
  .contact__item {
    display: flex;
    align-items: center;
    gap: 8px;
    font-size: 14px;
    letter-spacing: 0.4px;
  }
  .contact__item--web { font-weight: 700; font-size: 14px; }
  .contact__icon { width: 13px; height: 13px; fill: var(--teal); }
</style>
</head>
<body>
<main class="canvas">
  <section class="card card--front" aria-label="Card front">
    <div class="wordmark"><span>Silken Waves</span><span class="wordmark__dot"></span></div>
    <p class="business-name">Simply Silken Waves - Blow Dry Bar</p>
    <ul class="contact">
      <li class="contact__item">
        <svg class="contact__icon" viewBox="0 0 24 24" aria-hidden="true">
          <path d="M6.6 10.8c1.4 2.8 3.8 5.1 6.6 6.6l2.2-2.2c.3-.3.7-.4 1-.2 1.1.4 2.3.6 3.6.6.6 0 1 .4 1 1V20c0 .6-.4 1-1 1C10.6 21 3 13.4 3 4c0-.6.4-1 1-1h3.5c.6 0 1 .4 1 1 0 1.3.2 2.5.6 3.6.1.3 0 .7-.2 1L6.6 10.8z"/>
        </svg>
        <span>(555) 014-2763</span>
      </li>
      <li class="contact__item contact__item--web">
        <svg class="contact__icon" viewBox="0 0 24 24" aria-hidden="true">
          <path d="M12 2a10 10 0 1 0 0 20 10 10 0 0 0 0-20zm6.9 6h-2.9a15.7 15.7 0 0 0-1.4-3.6A8 8 0 0 1 18.9 8zM12 4c.8 1.2 1.5 2.5 1.9 4h-3.8c.4-1.5 1.1-2.8 1.9-4zM4.3 14a8.2 8.2 0 0 1 0-4h3.4a16.5 16.5 0 0 0 0 4H4.3zm.8 2h2.9c.3 1.3.8 2.5 1.4 3.6A8 8 0 0 1 5.1 16zM8 8H5.1a8 8 0 0 1 4.3-3.6C8.8 5.5 8.3 6.7 8 8zm4 12c-.8-1.2-1.5-2.5-1.9-4h3.8c-.4 1.5-1.1 2.8-1.9 4zm2.3-6H9.7a14.7 14.7 0 0 1 0-4h4.6a14.7 14.7 0 0 1 0 4zm.3 5.6c.6-1.1 1.1-2.3 1.4-3.6h2.9a8 8 0 0 1-4.3 3.6zM16.3 14a16.5 16.5 0 0 0 0-4h3.4a8.2 8.2 0 0 1 0 4h-3.4z"/>
        </svg>
        <span>WWW.SIMPLYSILKENWAVES.EXAMPLE</span>
      </li>
    </ul>
  </section>

  <section class="card card--back" aria-label="Card back">
    <div class="wordmark"><span>Silken Waves</span><span class="wordmark__dot"></span></div>
  </section>
</main>
</body>
</html>
```